Wellness Flyer

I am seeking a flyer for my health and wellness company, Orchard Vita. The flyer is to be DL size and single-sided. I am looking for a flyer that is both professional and fun looking, something similar to the uploaded files. Wording to include: (Please not wording to not include company name or logo but is rather advertising nutritional cleansing products)

Be your healthiest self. Take charge of your life. Get your best body.
Lose weight / Build muscle / Gain energy / Increase clarity
Start your journey to health and wellness. Transform your life
www.orchardvita.com.au
Mirela@orchardvita.com.au.
Natural . Raw. Organic . Cleansing system
Updates

Flyer needs to be single sided, DL size. I haven't uploaded my logo because I wanted to steer clear of having it on the flyer as it limits colour choice. Thanks.

Target Market(s)

Primarily Women 18-50.

Industry/Entity Type

Advertising

Font styles to use
Serif

Colors
34b8a4
fbed24

Requirements
Must have
• The wording as above.
Should not have
• Company name or Company logo

```html
<!DOCTYPE html>
<html lang="en">
<head>
<meta charset="utf-8">
<title>Orchard Vita – Wellness Flyer</title>
<link href="https://fonts.googleapis.com/css2?family=Lilita+One&family=Open+Sans:ital,wght@0,400;0,600;0,700;1,400&display=swap" rel="stylesheet">
<style>
  :root {
    --teal: #34b8a4;
    --teal-deep: #14897a;
    --teal-dark: #0e6f63;
    --teal-light: #7fd6c6;
    --yellow: #fbed24;
    --gold: #f9c93a;
    --amber: #f3a81c;
    --cream: #fff6d6;
    --white: #ffffff;
    --ink: #3b3b3b;
  }
  * { margin: 0; padding: 0; box-sizing: border-box; }
  html, body { width: 1200px; height: 2400px; overflow: hidden; background: var(--white); }
  .flyer { position: relative; width: 1200px; height: 2400px; overflow: hidden; font-family: "Open Sans", sans-serif; }
  .flyer-art { position: absolute; inset: 0; width: 1200px; height: 2400px; }

  .headline {
    position: absolute; right: 205px; top: 345px;
    text-align: right; font-family: "Lilita One", sans-serif;
    font-size: 86px; line-height: 128px; color: var(--teal-deep);
    -webkit-text-stroke: 3px var(--white); paint-order: stroke fill;
    text-shadow: 0 0 6px var(--white), 0 0 10px var(--white), 3px 4px 6px rgba(0,0,0,.25);
    letter-spacing: 1px;
  }

  .bubble-text {
    position: absolute; width: 340px; text-align: center;
    font-family: "Lilita One", sans-serif; font-size: 54px; line-height: 66px;
    color: var(--white); text-shadow: 2px 3px 0 var(--teal-dark), 0 0 10px rgba(0,0,0,.25);
    letter-spacing: 1px;
  }
  .bubble-text--charge { left: 185px; top: 1140px; }
  .bubble-text--body { left: 550px; top: 1140px; color: var(--teal-deep); text-shadow: 0 0 6px var(--white), 0 0 12px var(--white), 0 0 16px var(--white); }

  .benefit {
    position: absolute; width: 220px; text-align: center;
    font-family: "Lilita One", sans-serif; font-size: 36px; line-height: 44px;
    color: var(--teal-deep);
  }
  .benefit--weight  { left: 115px; top: 1920px; }
  .benefit--muscle  { left: 372px; top: 1905px; }
  .benefit--energy  { left: 628px; top: 1905px; }
  .benefit--clarity { left: 885px; top: 1905px; }

  .rsvp {
    position: absolute; left: 40px; top: 2128px; width: 128px; height: 40px;
    background: var(--teal-deep); color: var(--white);
    font-family: "Lilita One", sans-serif; font-size: 26px; line-height: 40px; text-align: center;
    border-radius: 4px 4px 0 0; letter-spacing: 2px;
  }
  .contact {
    position: absolute; left: 40px; right: 40px; top: 2168px; height: 56px;
    background: var(--white); display: flex; align-items: center;
    font-size: 36px; color: var(--ink); padding-left: 12px;
  }
  .contact .divider { display: inline-block; width: 3px; height: 40px; background: var(--ink); margin: 0 24px; }

  .tagline {
    position: absolute; left: 0; right: 0; top: 2292px; height: 66px;
    text-align: center; font-size: 43px; line-height: 66px; font-weight: 700; color: var(--teal-deep);
  }
</style>
</head>
<body>
<main class="flyer">
  <svg class="flyer-art" viewBox="0 0 1200 2400">
    <defs>
      <linearGradient id="photoTone" x1="0" y1="0" x2="0" y2="1">
        <stop offset="0" stop-color="#e9f4f2"/>
        <stop offset="0.35" stop-color="#cfe6d6"/>
        <stop offset="0.6" stop-color="#a9d36a"/>
        <stop offset="1" stop-color="#8cc43c"/>
      </linearGradient>
      <linearGradient id="warmBase" x1="0" y1="0" x2="0" y2="1">
        <stop offset="0" stop-color="#fde58a"/>
        <stop offset="0.5" stop-color="var(--gold)"/>
        <stop offset="1" stop-color="var(--amber)"/>
      </linearGradient>
      <linearGradient id="tealSweep" x1="0" y1="0" x2="1" y2="1">
        <stop offset="0" stop-color="var(--teal-light)"/>
        <stop offset="0.5" stop-color="var(--teal)"/>
        <stop offset="1" stop-color="var(--teal-deep)"/>
      </linearGradient>
      <radialGradient id="bubbleFill" cx="0.5" cy="0.4" r="0.6">
        <stop offset="0" stop-color="var(--teal-light)"/>
        <stop offset="0.6" stop-color="var(--teal)"/>
        <stop offset="1" stop-color="var(--teal-deep)"/>
      </radialGradient>
      <radialGradient id="bubbleFillSoft" cx="0.5" cy="0.45" r="0.6">
        <stop offset="0" stop-color="#ffffff"/>
        <stop offset="0.45" stop-color="#c9ece5"/>
        <stop offset="1" stop-color="var(--teal)"/>
      </radialGradient>
      <clipPath id="chargeClip"><circle cx="350" cy="1265" r="190"/></clipPath>
      <path id="ribbonCurve" d="M120,1720 Q600,1600 1080,1640"/>
      <path id="transformCurve" d="M0,1795 Q600,1660 1200,1750"/>
    </defs>

    <rect class="base-warm" x="0" y="0" width="1200" height="2400" fill="url(#warmBase)"/>

    <path class="hero-photo" role="img" aria-label="Photo of a smiling woman in a mint tank top stretching on green grass in a park, city skyline behind"
          d="M0,0 H1200 V860 Q700,1060 0,1300 Z" fill="url(#photoTone)"/>

    <polygon class="corner-teal" points="740,0 1200,0 1200,520" fill="url(#tealSweep)"/>
    <polygon class="corner-teal-light" points="820,0 1200,0 1200,330" fill="var(--teal)" opacity=".55"/>
    <polygon class="corner-gold" points="0,0 150,0 0,70" fill="var(--gold)"/>
    <polygon class="corner-teal-left" points="0,0 70,0 0,40" fill="var(--teal)"/>

    <path class="sweep-teal" d="M1200,820 Q720,1050 0,1240 V1330 Q720,1140 1200,1000 Z" fill="url(#tealSweep)"/>
    <path class="sweep-white" d="M1200,1000 Q700,1160 0,1340 V1380 Q700,1200 1200,1060 Z" fill="var(--white)" opacity=".8"/>
    <path class="sweep-cream" d="M0,1380 Q500,1260 1200,1060 V1400 Q700,1420 0,1500 Z" fill="var(--cream)" opacity=".45"/>

    <!-- take charge callout -->
    <g class="callout-charge">
      <circle cx="350" cy="1265" r="210" fill="var(--white)"/>
      <g clip-path="url(#chargeClip)">
        <rect x="150" y="1065" width="400" height="400" fill="url(#bubbleFill)"/>
        <path d="M150,1350 Q350,1420 550,1300 V1330 Q350,1450 150,1385 Z" fill="var(--white)"/>
        <path d="M150,1385 Q350,1450 550,1330 V1470 H150 Z" fill="var(--teal)"/>
      </g>
    </g>
    <!-- best body callout -->
    <circle cx="718" cy="1260" r="200" fill="var(--white)"/>
    <circle cx="718" cy="1260" r="180" fill="url(#bubbleFillSoft)"/>

    <!-- journey ribbon -->
    <path class="ribbon-teal" d="M0,1700 Q600,1560 1200,1640 V1770 Q600,1700 0,1800 Z" fill="var(--teal-deep)"/>
    <path class="ribbon-white" d="M0,1660 Q600,1520 1200,1600 V1700 Q600,1630 0,1760 Z" fill="var(--white)"/>
    <text font-family="Open Sans, sans-serif" font-size="44" fill="var(--teal-deep)">
      <textPath href="#ribbonCurve" startOffset="50%" text-anchor="middle">Start your journey to health and wellness</textPath>
    </text>
    <text font-family="Open Sans, sans-serif" font-size="34" font-style="italic" fill="var(--white)">
      <textPath href="#transformCurve" startOffset="50%" text-anchor="middle">Transform your life</textPath>
    </text>

    <!-- benefit diamonds -->
    <g class="benefit-diamonds" stroke-linejoin="round">
      <g transform="translate(225,1948)">
        <polygon points="0,-140 150,0 0,140 -150,0" fill="var(--teal-deep)" stroke="var(--teal-deep)" stroke-width="40" transform="translate(8,10)"/>
        <polygon points="0,-140 150,0 0,140 -150,0" fill="var(--white)" stroke="var(--white)" stroke-width="40"/>
      </g>
      <g transform="translate(482,1948)">
        <polygon points="0,-140 150,0 0,140 -150,0" fill="var(--teal-deep)" stroke="var(--teal-deep)" stroke-width="40" transform="translate(8,10)"/>
        <polygon points="0,-140 150,0 0,140 -150,0" fill="var(--white)" stroke="var(--white)" stroke-width="40"/>
      </g>
      <g transform="translate(738,1948)">
        <polygon points="0,-140 150,0 0,140 -150,0" fill="var(--teal-deep)" stroke="var(--teal-deep)" stroke-width="40" transform="translate(8,10)"/>
        <polygon points="0,-140 150,0 0,140 -150,0" fill="var(--white)" stroke="var(--white)" stroke-width="40"/>
      </g>
      <g transform="translate(995,1948)">
        <polygon points="0,-140 150,0 0,140 -150,0" fill="var(--teal-deep)" stroke="var(--teal-deep)" stroke-width="40" transform="translate(8,10)"/>
        <polygon points="0,-140 150,0 0,140 -150,0" fill="var(--white)" stroke="var(--white)" stroke-width="40"/>
      </g>
    </g>
    <g class="chevron-icons" fill="none" stroke="var(--white)" stroke-width="6" stroke-linecap="round" stroke-linejoin="round">
      <g transform="translate(225,1872)"><circle r="28" fill="var(--teal)" stroke="var(--teal-deep)" stroke-width="4"/><path d="M-12,-10 L0,2 L12,-10 M-12,2 L0,14 L12,2"/></g>
      <g transform="translate(482,1862)"><circle r="28" fill="var(--teal)" stroke="var(--teal-deep)" stroke-width="4"/><path d="M-12,-10 L0,2 L12,-10 M-12,2 L0,14 L12,2"/></g>
      <g transform="translate(738,1862)"><circle r="28" fill="var(--teal)" stroke="var(--teal-deep)" stroke-width="4"/><path d="M-12,-10 L0,2 L12,-10 M-12,2 L0,14 L12,2"/></g>
      <g transform="translate(995,1862)"><circle r="28" fill="var(--teal)" stroke="var(--teal-deep)" stroke-width="4"/><path d="M-12,-10 L0,2 L12,-10 M-12,2 L0,14 L12,2"/></g>
    </g>

    <rect x="0" y="2262" width="1200" height="6" fill="var(--white)"/>
    <rect x="0" y="2276" width="1200" height="4" fill="var(--white)" opacity=".8"/>
    <rect x="0" y="2288" width="1200" height="74" fill="var(--yellow)" opacity=".75"/>
    <rect x="0" y="2362" width="1200" height="38" fill="var(--cream)"/>
  </svg>

  <h1 class="headline">BE<br>YOUR<br>HEALTHIEST<br>SELF</h1>

  <p class="bubble-text bubble-text--charge">TAKE<br>CHARGE OF<br>YOUR LIFE</p>
  <p class="bubble-text bubble-text--body">GET<br>YOUR BEST<br>BODY</p>

  <p class="benefit benefit--weight">Lose<br>weight</p>
  <p class="benefit benefit--muscle">Build<br>muscle</p>
  <p class="benefit benefit--energy">Gain<br>energy</p>
  <p class="benefit benefit--clarity">Increase<br>clarity</p>

  <div class="rsvp">R.S.V.P</div>
  <p class="contact">Mirela@orchardvita.com.au<span class="divider"></span>www.orchardvita.com.au</p>

  <p class="tagline">Natural • Raw • Organic • Cleansing system</p>
</main>
</body>
</html>
```